Military training songs recorded live with troops.

I need a graphic designer (and website builder) to create the artwork, logo and website for a new company marketing campaign under the URL www.drillmoor.com.
This website will be devoted to featuring the audio catalog I created with my father in which we recorded live during PT training with troops of the R.L. Garrison.
Ultimately, I would like the website to be the one and only distribution site for our catalog. This will be the most effectively means in addressing piracy and copyright infringement. However, this would require a website platform which supports MP3 and financial sales software.
Thus, for now, the website can establish and feature the catalog we created and provide links just to Melodrop.
Thus in addition to a website, we would need graphics for the new covers for our catalog which contains 32 products.
I have attached a MP3 file to provide insight into the military cadences we recorded and have the exclusive rights to distribute and sell.

For the representation of military service to our entire society.

One-of-a-kind military training songs recorded live with troops during PT runs & marches.

• Lordcorps

Designer to choose only greyscale colors for use in the design.

• To feature the entire catalog by creating artwork for every product (cover art needed for 32 products) and separating the products under the various Armed Force: The R.L. Harbor Legion, the Army, the Air Force and the Navy. Every product must have a link for purchase from Melodrop.
• The ability to play MP3 files.
• N/A

```html
<!DOCTYPE html>
<html lang="en">
<head>
<meta charset="utf-8">
<title>Drillmoor — The Sound of Discipline</title>
<link rel="stylesheet" href="https://fonts.googleapis.com/css2?family=Playfair+Display:wght@400;500;700&family=Inter:wght@400;500&family=IBM+Plex+Mono:wght@400;500&display=swap">
<style>
:root{
  --bg:#0f0f0f;
  --bg-archive:#141414;
  --bg-legacy:#1a1a1a;
  --bg-collection:#121212;
  --bg-footer:#0b0b0b;
  --ink:#f1efe9;
  --ink-soft:#c9c7c3;
  --ink-dim:#7b7a78;
  --ink-faint:#4d4d4c;
  --accent:#8e8d8a;
  --accent-deep:#555453;
  --badge-bg:#2a2a29;
  --badge-ink:#6a6967;
  --line:#2c2c2b;
  --tile:#1f1f1f;
  --serif:"Playfair Display",Georgia,serif;
  --sans:"Inter",Helvetica,Arial,sans-serif;
  --mono:"IBM Plex Mono",Menlo,monospace;
}
*{margin:0;padding:0;box-sizing:border-box}
html,body{width:1200px;height:3396px;overflow:hidden;background:var(--bg);color:var(--ink)}
.abs{position:absolute}
section,header,footer{position:absolute;left:0;width:1200px}
.mono{font-family:var(--mono);text-transform:uppercase;letter-spacing:.14em}

/* Hero */
.hero{top:0;height:1042px;background:radial-gradient(ellipse at 50% 30%,#2a2a2a 0%,#1a1a1a 45%,#121212 100%)}
.hero-photo{left:0;top:620px;width:1200px;height:422px;background:linear-gradient(180deg,rgba(40,40,40,0) 0%,#262626 40%,#1b1b1b 70%,#131313 100%)}
.nav{top:0;height:76px}
.logo{font-family:var(--serif);font-size:27px;color:#bcbcba;letter-spacing:-.01em}
.nav .logo{left:68px;top:22px}
.nav-link{top:28px;font-family:var(--sans);font-size:13px;letter-spacing:.1em;color:var(--ink-dim)}
.nav-link.active{color:var(--ink-soft);border-bottom:1px solid var(--ink-soft);padding-bottom:4px}
.user-icon{left:1116px;top:26px}
.hero-title{left:0;width:1200px;text-align:center;font-family:var(--serif);font-weight:700;font-size:72px;line-height:76px;top:248px;letter-spacing:-.01em}
.hero-title .accent{color:var(--accent);display:block}
.hero-sub{left:0;width:1200px;text-align:center;top:414px;font-size:11px;color:var(--ink-soft)}
.btn-play{left:523px;top:464px;width:154px;height:41px;border-radius:21px;background:#ebebea;color:#151515;font-size:11px;line-height:41px;text-align:center}
.play-big{left:548px;top:551px}
.player{left:241px;top:703px;width:716px;height:165px;border:1px solid rgba(255,255,255,.05);border-radius:6px;background:rgba(30,30,30,.35)}
.time{top:815px;font-size:10px;color:var(--ink-dim)}
.time.current{color:var(--accent)}
.track{left:270px;top:839px;width:650px;height:1px;background:#3a3a3a}
.track-fill{left:270px;top:839px;width:238px;height:2px;background:var(--accent)}
.track-knob{left:502px;top:834px;width:12px;height:12px;border-radius:50%;background:var(--accent);border:2px solid var(--accent-deep)}

/* Archive */
.archive{top:1042px;height:920px;background:var(--bg-archive)}
.section-title{font-family:var(--serif);font-weight:700;font-size:48px;line-height:1.1;color:var(--ink)}
.archive .section-title{left:60px;top:120px}
.section-sub{font-size:11px;color:var(--ink-dim)}
.archive .section-sub{left:60px;top:189px}
.arrow-btn{top:153px;width:46px;height:46px;border:1px solid #5a5a59;border-radius:50%;display:flex;align-items:center;justify-content:center}
.card-art{top:261px;width:359px;height:359px;border:1px solid var(--line);border-radius:4px}
.card-art.boots{left:13px;background:radial-gradient(ellipse at 50% 45%,#5b5b5a 0%,#333 55%,#1d1d1d 100%)}
.card-art.active{left:402px;height:352px;background:radial-gradient(ellipse at 50% 40%,#2a2a2a 0%,#1a1a1a 100%);box-shadow:0 20px 40px rgba(0,0,0,.5)}
.card-art.tags{left:793px;background:radial-gradient(ellipse at 55% 55%,#6a6a69 0%,#3a3a3a 45%,#1d1d1d 100%)}
.card-play{left:545px;top:354px;width:74px;height:74px;border-radius:50%;background:#efefed;display:flex;align-items:center;justify-content:center}
.listen{left:402px;width:359px;text-align:center;top:458px;font-size:11px;letter-spacing:.25em;color:var(--ink)}
.card-links{top:500px;font-size:9px;color:var(--ink-dim);letter-spacing:.08em}
.badge{top:652px;font-size:8px;padding:3px 8px;border-radius:2px;background:var(--badge-bg);color:var(--badge-ink)}
.badge.rare{background:#3a3a39;color:#5f5f5e}
.card-meta{top:679px;font-size:11px;color:var(--ink-faint)}
.card-title{top:700px;font-family:var(--serif);font-size:31px;color:var(--ink)}

/* Legacy */
.legacy{top:1962px;height:801px;background:var(--bg-legacy)}
.legacy-photo{left:60px;top:120px;width:494px;height:562px;background:radial-gradient(ellipse at 45% 55%,#4d4d4c 0%,#2c2c2c 55%,#161616 100%)}
.fragment{left:313px;top:471px;width:241px;height:154px;background:#222;border:1px solid #2e2e2e;padding:24px 0 0 32px}
.fragment .mono{font-size:9px;color:var(--accent);letter-spacing:.1em}
.fragment p{margin-top:18px;font-family:var(--sans);font-size:13px;line-height:20px;color:var(--ink-soft);width:205px}
.eyebrow{left:645px;top:170px;font-size:11px;color:var(--accent);display:flex;align-items:center;gap:14px}
.eyebrow::before{content:"";width:45px;height:1px;background:var(--accent)}
.legacy .section-title{left:645px;top:212px;width:520px;font-size:46px;line-height:56px}
.legacy-copy{left:645px;top:358px;width:482px;font-family:var(--sans);font-size:16.5px;line-height:27.5px;color:var(--ink-soft)}
.legacy-copy p+p{margin-top:28px}
.legacy-rule{left:645px;top:590px;width:494px;height:1px;background:var(--line)}
.origin-link{left:645px;top:616px;font-size:11px;color:var(--ink);display:flex;align-items:center;gap:14px}

/* Collection */
.collection{top:2763px;height:329px;background:var(--bg-collection)}
.collection .section-title{left:60px;top:98px;font-size:46px;line-height:53px}
.collection-meta{left:99px;top:216px;width:300px;font-size:11px;letter-spacing:.1em;line-height:13px;color:var(--ink-dim);text-transform:none}
.collection-meta::before{content:"";position:absolute;left:-39px;top:12px;width:30px;height:1px;background:var(--line)}
.format{top:93px;width:149px;height:148px;background:var(--tile);text-align:center;padding-top:54px}
.format .mono{font-size:9px;color:var(--ink-dim);letter-spacing:.1em}
.format h3{margin-top:10px;font-family:var(--serif);font-weight:400;font-size:20px;color:var(--ink-soft)}
.format.vinyl{border-radius:50%}
.format.digital{border:1px solid #3a3a3a;border-radius:8px}
.format.box{background:radial-gradient(ellipse at 50% 40%,#383838 0%,#222 100%)}

/* Footer */
.footer{top:3092px;height:304px;background:var(--bg-footer)}
.footer .logo{left:60px;top:130px;color:var(--ink)}
.footer-tag{left:60px;top:172px;font-family:var(--mono);font-size:9px;color:var(--ink-dim)}
.footer-link{top:151px;font-size:11px;color:var(--ink-soft)}
.copyright{right:61px;top:151px;font-size:10px;color:var(--ink-dim)}
</style>
</head>
<body>

<section class="hero">
  <div class="abs hero-photo" role="img" aria-label="Silhouettes of troops running through fog at dawn"></div>

  <header class="nav">
    <div class="abs logo">DRILLMOOR</div>
    <a class="abs nav-link active" style="left:483px">ARCHIVE</a>
    <a class="abs nav-link" style="left:591px">LEGACY</a>
    <a class="abs nav-link" style="left:692px">CADENCES</a>
    <a class="abs nav-link" style="left:815px">ABOUT</a>
    <svg class="abs user-icon" width="24" height="24" viewBox="0 0 24 24" fill="none" stroke="#b5b5b3" stroke-width="1.5"><circle cx="12" cy="12" r="10"/><circle cx="12" cy="10" r="3.5"/><path d="M5.5 18.5c1.6-2.4 3.9-3.5 6.5-3.5s4.9 1.1 6.5 3.5"/></svg>
  </header>

  <h1 class="abs hero-title">THE SOUND OF<span class="accent">DISCIPLINE</span></h1>
  <div class="abs hero-sub mono">Live military cadences. Recorded. Preserved. Shared.</div>
  <a class="abs btn-play mono">Play archive</a>

  <svg class="abs play-big" width="104" height="104" viewBox="0 0 104 104"><circle cx="52" cy="52" r="51" fill="#1d1d1d" stroke="#2e2e2e" stroke-width="2"/><path d="M45 40v24l19-12z" fill="#f1efe9"/></svg>

  <div class="abs player"></div>
  <div class="abs time current mono" style="left:279px">01:24</div>
  <div class="abs time mono" style="left:889px">03:45</div>
  <div class="abs track"></div>
  <div class="abs track-fill"></div>
  <div class="abs track-knob"></div>
</section>

<section class="archive">
  <h2 class="abs section-title">THE ARCHIVE</h2>
  <div class="abs section-sub mono">Restored field recordings</div>
  <div class="abs arrow-btn" style="left:1033px"><svg width="18" height="18" viewBox="0 0 18 18" fill="none" stroke="#e6e6e4" stroke-width="1.6"><path d="M15 9H3M8 4 3 9l5 5"/></svg></div>
  <div class="abs arrow-btn" style="left:1093px"><svg width="18" height="18" viewBox="0 0 18 18" fill="none" stroke="#e6e6e4" stroke-width="1.6"><path d="M3 9h12M10 4l5 5-5 5"/></svg></div>

  <div class="abs card-art boots" role="img" aria-label="Worn combat boots on gravel"></div>
  <div class="abs card-art active" role="img" aria-label="Dim night scene of paratroopers"></div>
  <div class="abs card-play"><svg width="22" height="22" viewBox="0 0 22 22"><path d="M6 3v16l13-8z" fill="#151515"/></svg></div>
  <div class="abs listen mono">▸ Listen now</div>
  <div class="abs card-links mono" style="left:524px">→ Story</div>
  <div class="abs card-links mono" style="left:594px">↗ Melodrop</div>
  <div class="abs card-art tags" role="img" aria-label="Close-up of metal identification tags"></div>

  <span class="abs badge mono" style="left:60px">Restored audio</span>
  <div class="abs card-meta mono" style="left:60px">1987 · Army</div>
  <div class="abs card-title" style="left:60px">Morning Run</div>

  <span class="abs badge rare mono" style="left:450px">Rare record</span>
  <div class="abs card-meta mono" style="left:450px">1968 · Air Force</div>
  <div class="abs card-title" style="left:450px">Night Jump</div>

  <span class="abs badge mono" style="left:840px">Remastered</span>
  <div class="abs card-meta mono" style="left:840px">1992 · Harbor Legion</div>
  <div class="abs card-title" style="left:840px">The Grinder</div>
</section>

<section class="legacy">
  <div class="abs legacy-photo" role="img" aria-label="Vintage field tape recorder in a barracks room"></div>
  <div class="abs fragment">
    <div class="mono">Archive fragment · 1987</div>
    <p>"...the cadence isn't just rhythm. It's the collective breath of fifty men moving as one."</p>
  </div>

  <div class="abs eyebrow mono">The legacy</div>
  <h2 class="abs section-title">PRESERVING THE ECHOES OF DUTY</h2>
  <div class="abs legacy-copy">
    <p>These recordings were never intended to become products. They began as a way to preserve moments of effort, rhythm, and shared endurance. Today, they remain exactly as they were captured.</p>
    <p>They are raw, visceral audio documents captured on the march, representing the sound of discipline and endurance.</p>
  </div>
  <div class="abs legacy-rule"></div>
  <a class="abs origin-link mono">Read the origin story <svg width="16" height="12" viewBox="0 0 16 12" fill="none" stroke="#f1efe9" stroke-width="1.6"><path d="M1 6h13M9 1l5 5-5 5"/></svg></a>
</section>

<section class="collection">
  <h2 class="abs section-title">THE<br>COLLECTION</h2>
  <div class="abs collection-meta mono">32 recordings | 9 hours preserved | 1987–1998</div>

  <div class="abs format" style="left:481px"><div class="mono">Type 01</div><h3>Cassette</h3></div>
  <div class="abs format vinyl" style="left:650px"><div class="mono">Type 02</div><h3>Vinyl</h3></div>
  <div class="abs format digital" style="left:821px"><div class="mono">Type 03</div><h3>Digital</h3></div>
  <div class="abs format box" style="left:990px" role="img" aria-label="Stacked archive tape boxes"><div class="mono">Type 04</div><h3>Archive Box</h3></div>
</section>

<footer class="footer">
  <div class="abs logo">DRILLMOOR</div>
  <div class="abs footer-tag">Preserving the rhythm of endurance.</div>
  <a class="abs footer-link mono" style="left:413px">Terms</a>
  <a class="abs footer-link mono" style="left:483px">Privacy</a>
  <a class="abs footer-link mono" style="left:567px">Contact</a>
  <div class="abs copyright mono">© 2026 Drillmoor archive. All rights reserved.</div>
</footer>

</body>
</html>
```